Spooky Sweets Night

I am an intern at Marlow Ridge Community College, and Campus Council is hosting a Spooky Sweets Night in the Johnson County area. I am looking for a digital flyer to use for the event. Here are details for this year's event and info from last year. If you have any questions, please let me know. Last year's flyer is attached below.

Date: Friday, Oct. 25th, 2019
Location: Pellham Hall (Ground Floor)
Theme: Cats & Bats
Exciting Activities Include:
-(Glowing) Footsteps showing the path the kids should go?
-Face painting
-Cotton Candy
-Fog Machine w/bubbles
-Candy sponsorship (Fresko or Oak Basket)
-Encouraging the community to bring food donations for MRCC Food Pantry

```html
<!DOCTYPE html>
<html lang="en">
<head>
<meta charset="UTF-8">
<title>Spooky Sweets Night – Flyer</title>
<link rel="stylesheet" href="https://fonts.googleapis.com/css2?family=Chewy&family=Mystery+Quest&family=Fredoka:wght@500&display=swap">
<style>
  :root {
    --backdrop: #2f2b2a;
    --flyer-orange: #e8602a;
    --panel-dark: #3b3534;
    --title-yellow: #f3d22e;
    --accent-orange: #f29a2e;
    --accent-red: #ee5a2c;
    --text-light: #f4efe8;
    --moon-pale: #d9ddd0;
    --moon-shadow: #8f948a;
    --bat-navy: #232a45;
    --cat-black: #1b1818;
  }
  * { box-sizing: border-box; margin: 0; padding: 0; }
  html, body { width: 1200px; height: 800px; overflow: hidden; }
  body { background: var(--backdrop); position: relative; }

  .flyer {
    position: absolute; left: 360px; top: 40px;
    width: 480px; height: 720px;
    background: var(--flyer-orange);
  }
  .flyer__panel {
    position: absolute; inset: 24px;
    background: var(--panel-dark);
    border-radius: 46px;
  }
  .flyer__moon-scene {
    position: absolute; left: 150px; top: 50px;
    width: 220px; height: 220px; border-radius: 50%;
    background: radial-gradient(circle at 45% 40%, var(--moon-pale) 0%, var(--moon-shadow) 70%, var(--panel-dark) 100%);
  }
  .flyer__bat {
    position: absolute; left: 14px; top: 10px;
    width: 170px; height: 150px; border-radius: 50% 50% 40% 40%;
    background: linear-gradient(160deg, var(--bat-navy), #3a4569);
  }
  .flyer__cat {
    position: absolute; left: 372px; top: 560px;
    width: 80px; height: 140px; border-radius: 40px 40px 10px 10px;
    background: var(--cat-black);
  }

  .sponsor {
    position: absolute; left: 60px; top: 218px; width: 110px;
    text-align: center; color: var(--text-light);
  }
  .sponsor__label { font: 11px/1.1 "Mystery Quest", cursive; }
  .sponsor__names {
    margin-top: 6px; display: flex; align-items: center; gap: 6px; justify-content: center;
    font: 16px/1.05 "Mystery Quest", cursive; color: var(--accent-orange);
  }
  .sponsor__dot { width: 10px; height: 10px; border-radius: 50%; background: var(--accent-red); flex: none; }

  .event-title {
    position: absolute; left: 170px; top: 262px; width: 230px;
    font: 40px/0.9 "Chewy", cursive; color: var(--title-yellow);
    text-align: center; transform: rotate(4deg);
  }

  .activities {
    position: absolute; left: 40px; top: 392px; width: 400px;
    display: flex; justify-content: center; gap: 10px;
    font: 17px/1 "Mystery Quest", cursive; color: var(--accent-orange);
  }
  .activities__sep { color: var(--text-light); }
  .activities__note { display: block; font-size: 10px; text-align: right; }

  .footsteps {
    position: absolute; left: 100px; top: 428px; width: 280px;
    text-align: center; font: 17px/1.05 "Mystery Quest", cursive; color: var(--accent-red);
  }

  .details {
    position: absolute; left: 90px; width: 300px; text-align: center;
    font: 500 18px/1 "Fredoka", sans-serif; color: var(--text-light);
    display: flex; align-items: center; justify-content: center; gap: 8px;
  }
  .details--date { top: 486px; }
  .details--place { top: 528px; }
  .details svg { width: 18px; height: 18px; flex: none; }

  .donation {
    position: absolute; left: 120px; top: 580px; width: 240px;
    text-align: center; font: 15px/1.05 "Mystery Quest", cursive; color: var(--accent-red);
  }
  .donation__cause {
    display: block; margin-top: 8px;
    font-size: 24px; color: var(--title-yellow);
  }
</style>
</head>
<body>
  <article class="flyer">
    <div class="flyer__panel"></div>
    <div class="flyer__moon-scene" role="img" aria-label="Full moon with a haunted house, bats and a flying witch"></div>
    <div class="flyer__bat" role="img" aria-label="Cartoon bat with spread wings"></div>

    <div class="sponsor">
      <p class="sponsor__label">Candy sponsor<br>by</p>
      <p class="sponsor__names"><span class="sponsor__dot"></span>Fresko<br>or<br>Oak Basket</p>
    </div>

    <h1 class="event-title">Spooky Sweets Night</h1>

    <p class="activities">
      <span>Face Painting</span><span class="activities__sep">|</span>
      <span>Cotton Candy</span><span class="activities__sep">|</span>
      <span>Fog Machine<span class="activities__note">w/ Bubbles</span></span>
    </p>

    <p class="footsteps">(Glowing) Footsteps showing the path the kids should go?</p>

    <p class="details details--date">Friday, Oct. 25th, 2019
      <svg viewBox="0 0 20 20" fill="none" stroke="#f29a2e" stroke-width="1.6"><rect x="2" y="4" width="16" height="14" rx="2"/><line x1="2" y1="8" x2="18" y2="8"/><line x1="6" y1="2" x2="6" y2="6"/><line x1="14" y1="2" x2="14" y2="6"/></svg>
    </p>
    <p class="details details--place">Pellham Hall (Ground Floor)
      <svg viewBox="0 0 20 20" fill="none" stroke="#f29a2e" stroke-width="1.6"><path d="M10 18s6-6 6-10a6 6 0 0 0-12 0c0 4 6 10 6 10z"/><circle cx="10" cy="8" r="2"/></svg>
    </p>

    <p class="donation">Encouraging<br>the community<br>to bring food donations<br>for
      <span class="donation__cause">MRCC Food Pantry</span>
    </p>

    <div class="flyer__cat" role="img" aria-label="Black cat holding a fish skeleton"></div>
  </article>
</body>
</html>
```